Design trifold flyer for patients

Hi buddy,I need a trifold brochure for an early event that month. I just need a design template in Adobe Illustrator, so that I can modify it later.Size: A4 divide into 3 pages, 10x21cm each. The total has 6 page with both sides.Content: (Page)1. Cover with logo, address, phone number, etc..2. Instruction: An image and a paragraph3 + 4. A content list, paragraph5. Note with patients6. Price listColor: blue and light blue, greenTarget audience: Patients

Target Market(s)

Patients in hospital

Industry/Entity Type

Medical

Font styles to use
Sans Serif

Colors
85cae6
33b8a4
0692cd

Requirements
Must have
• picture place holder
Nice to have
• icon

```html
<!DOCTYPE html>
<html lang="en">
<head>
<meta charset="utf-8">
<title>Patient Trifold Brochure</title>
<link rel="stylesheet" href="https://fonts.googleapis.com/css2?family=Roboto+Condensed:wght@400;500&family=Arimo:wght@400&display=swap">
<style>
  :root {
    --navy: #213f8a;
    --slate: #4f64a0;
    --mid-blue: #1a5ba3;
    --deep-blue: #0f7bbd;
    --blue: #0692cd;
    --sky: #1f9ad4;
    --soft-blue: #4fb3dd;
    --light-blue: #85cae6;
    --teal: #33b5a4;
    --stripe-teal: #2ba9a8;
    --lavender: #b8c0d6;
    --frost: #ffffff;
    --grey: #b3b3b3;
    --ink: #111111;
    --page: #ffffff;
  }
  html, body {
    margin: 0;
    padding: 0;
    width: 730px;
    height: 1200px;
    overflow: hidden;
    background: var(--page);
  }
  .brochure { display: block; width: 730px; height: 1200px; }
  .heading-text { font-family: "Roboto Condensed", sans-serif; font-size: 29px; fill: var(--ink); }
  .tab-text { font-family: "Arimo", sans-serif; font-size: 22px; fill: var(--ink); }
  .contact-text { font-family: "Arimo", sans-serif; font-size: 14.5px; fill: var(--ink); }
  .body-text { font-family: "Arimo", sans-serif; font-size: 24px; fill: var(--ink); }
  .brand-name { font-family: "Roboto Condensed", sans-serif; font-weight: 500; font-size: 27px; fill: var(--navy); }
  .placeholder-label { font-family: "Roboto Condensed", sans-serif; font-weight: 500; font-size: 44px; fill: var(--frost); }
  .frost-panel { fill: var(--frost); opacity: 0.68; }
</style>
</head>
<body>
<svg class="brochure" viewBox="0 0 913 1500" preserveAspectRatio="none" xmlns="http://www.w3.org/2000/svg">

  <!-- OUTSIDE SPREAD -->
  <g class="outside-spread">
    <!-- Notes for patients panel -->
    <g class="notes-panel">
      <rect x="8" y="0" width="122" height="253" fill="var(--slate)"/>
      <rect x="8" y="253" width="122" height="377" fill="var(--navy)"/>
      <rect x="130" y="0" width="73" height="630" fill="var(--navy)"/>
      <rect x="103" y="310" width="100" height="320" fill="var(--mid-blue)"/>
      <rect x="203" y="0" width="105" height="630" fill="var(--blue)"/>
      <rect class="frost-panel" x="36" y="107" width="254" height="423"/>
      <text class="heading-text" x="165" y="254" text-anchor="middle">Notes for patients</text>
      <text class="heading-text" x="165" y="287" text-anchor="middle">will be in this area</text>
    </g>

    <!-- Price list panel -->
    <g class="price-panel">
      <rect x="308" y="0" width="302" height="630" fill="var(--navy)"/>
      <rect x="333" y="27" width="254" height="69" fill="var(--lavender)"/>
      <text class="tab-text" x="452" y="71" text-anchor="middle">Price List</text>
      <rect x="316" y="121" width="143" height="509" fill="var(--deep-blue)"/>
      <rect x="459" y="121" width="143" height="509" fill="var(--teal)"/>

      <g class="stethoscope-icon">
        <circle cx="535" cy="171" r="34" fill="var(--blue)"/>
        <path d="M535 137 A34 34 0 0 1 535 205 Z" fill="var(--deep-blue)"/>
        <path d="M527 150 v12 a9 9 0 0 0 18 0 v-12" fill="none" stroke="var(--frost)" stroke-width="3" stroke-linecap="round"/>
        <path d="M536 171 v9 a8 8 0 0 1 -16 0 v-2" fill="none" stroke="var(--frost)" stroke-width="3" stroke-linecap="round"/>
        <circle cx="520" cy="186" r="4" fill="none" stroke="var(--frost)" stroke-width="2.5"/>
      </g>

      <rect class="frost-panel" x="338" y="209" width="247" height="325"/>
      <text class="heading-text" x="462" y="343" text-anchor="middle">Prices list content</text>
      <text class="heading-text" x="456" y="376" text-anchor="middle">will be in this area</text>

      <g class="heart-icon">
        <circle cx="381" cy="579" r="40" fill="var(--blue)"/>
        <path d="M381 539 A40 40 0 0 1 381 619 Z" fill="#0a86b8"/>
        <path d="M381 594 C364 582 362 572 366 566 C370 560 378 561 381 567 C384 561 392 560 396 566 C400 572 398 582 381 594 Z" fill="var(--frost)"/>
      </g>
    </g>

    <!-- Cover panel -->
    <g class="cover-panel">
      <rect x="610" y="0" width="303" height="630" fill="var(--light-blue)"/>
      <rect x="631" y="0" width="41" height="44" fill="var(--sky)"/>
      <rect x="798" y="30" width="54" height="71" fill="var(--soft-blue)"/>
      <rect x="830" y="0" width="53" height="73" fill="var(--blue)"/>
      <rect x="696" y="77" width="53" height="72" fill="var(--soft-blue)"/>
      <rect x="627" y="285" width="41" height="43" fill="var(--sky)"/>
      <polygon points="610,372 913,240 913,272 610,402" fill="var(--blue)"/>
      <polygon points="610,402 913,272 913,306 610,440" fill="var(--stripe-teal)"/>

      <text class="brand-name" x="764" y="228" text-anchor="middle">Hanbit Medical Center</text>

      <g class="contact-box">
        <rect x="654" y="544" width="58" height="86" fill="var(--blue)"/>
        <rect x="654" y="618" width="240" height="12" fill="var(--blue)"/>
        <rect x="829" y="483" width="65" height="147" fill="var(--blue)"/>
        <rect class="frost-panel" x="665" y="425" width="221" height="193"/>
        <text class="contact-text" x="675" y="459">Address would  be included in</text>
        <text class="contact-text" x="679" y="475">this area</text>
        <text class="contact-text" x="682" y="527">Phone Number will go here</text>
        <text class="contact-text" x="683" y="583">Website link will go here</text>
      </g>
    </g>
  </g>

  <!-- INSIDE SPREAD -->
  <g class="inside-spread">
    <!-- Instruction panel -->
    <g class="instruction-panel">
      <rect x="0" y="870" width="300" height="630" fill="var(--light-blue)"/>
      <g class="image-placeholder" role="img" aria-label="Picture placeholder for instruction image">
        <rect x="12" y="870" width="280" height="392" fill="var(--grey)"/>
        <line x1="25" y1="870" x2="292" y2="1225" stroke="var(--frost)" stroke-width="5"/>
        <line x1="290" y1="870" x2="95" y2="1135" stroke="var(--frost)" stroke-width="5"/>
        <text class="placeholder-label" x="160" y="1064" text-anchor="middle">PLACEHOLDER</text>
      </g>
      <polygon points="0,1078 300,1262 300,1500 0,1500" fill="var(--light-blue)"/>
      <polygon points="8,1093 292,1275 292,1490 8,1490" fill="var(--blue)"/>
      <text class="body-text" x="40" y="1323">Paragraph</text>
      <text class="body-text" x="40" y="1379">will go in this area</text>
    </g>

    <!-- Content panel one -->
    <g class="content-panel-one">
      <rect x="300" y="870" width="303" height="630" fill="var(--navy)"/>
      <rect x="329" y="899" width="248" height="326" fill="var(--blue)"/>
      <text class="body-text" x="385" y="980">Content List</text>
      <text class="body-text" x="385" y="1033">will go in this</text>
      <text class="body-text" x="385" y="1086">area</text>
      <rect x="326" y="1248" width="258" height="240" fill="var(--lavender)"/>
      <text class="body-text" x="373" y="1314">Paragraph will</text>
      <text class="body-text" x="373" y="1367">go in this area</text>
    </g>

    <!-- Content panel two -->
    <g class="content-panel-two">
      <rect x="603" y="870" width="310" height="630" fill="var(--blue)"/>
      <polygon points="617,870 890,870 890,1073 615,1247" fill="var(--light-blue)"/>
      <polygon points="612,1275 897,1090 895,1488 612,1488" fill="var(--light-blue)"/>
      <text class="body-text" x="677" y="971">Content List</text>
      <text class="body-text" x="677" y="1024">will go in this</text>
      <text class="body-text" x="677" y="1077">area</text>
      <text class="body-text" x="688" y="1312">Paragraph will</text>
      <text class="body-text" x="688" y="1365">go in this area</text>
    </g>
  </g>
</svg>
</body>
</html>
```